Business Cards for accounting firm

Need a file and design that we can update for our employees when we get a design we like. Logo is attached.
Megan Tolliver CPA
Owner
P.O. Box 418
Halden Falls WI 53187
5553628405
megan@brightlanefin.com
www.brightlanefin.com
Accounting

```html
<!DOCTYPE html>
<html lang="en">
<head>
<meta charset="utf-8">
<title>Brightlane Financial – Business Cards</title>
<link href="https://fonts.googleapis.com/css2?family=Arimo:wght@400;700&display=swap" rel="stylesheet">
<style>
  :root {
    --page-bg: #e9e6e1;
    --card-light-top: #ffffff;
    --card-light-bottom: #dcdcdc;
    --card-dark: #0d0d0d;
    --card-dark-sheen: #2a2a2a;
    --rule-dark: #111111;
    --rule-light: #f4f4f4;
    --logo-grey: #8c8c8c;
    --name-white: #ffffff;
    --meta-grey: #9a9a9a;
    --contact-grey: #b5b5b5;
  }
  * { margin: 0; padding: 0; box-sizing: border-box; }
  html, body {
    width: 1200px; height: 892px; overflow: hidden;
    background: var(--page-bg);
    font-family: "Arimo", Arial, sans-serif;
  }
  .sheet {
    width: 1200px; height: 892px;
    display: flex; align-items: center; justify-content: center; gap: 90px;
  }
  .card {
    position: relative;
    width: 320px; height: 560px;
    background: var(--card-dark);
    overflow: hidden;
    box-shadow: 0 14px 30px rgba(0,0,0,0.28);
    display: flex; flex-direction: column;
  }
  .card__light {
    background: linear-gradient(180deg, var(--card-light-top), var(--card-light-bottom));
    display: flex; flex-direction: column; justify-content: center; align-items: center;
    padding: 0 24px;
  }
  .card--front .card__light { height: 200px; }
  .card--back .card__light { height: 290px; }
  .card__rule {
    height: 16px;
    background:
      linear-gradient(var(--rule-dark), var(--rule-dark)) 0 4px / 100% 3px no-repeat,
      linear-gradient(var(--rule-light), var(--rule-light)) 0 11px / 100% 3px no-repeat,
      linear-gradient(180deg, var(--card-light-bottom) 0 8px, var(--card-dark) 8px 16px);
  }
  .card__dark {
    flex: 1;
    background: linear-gradient(160deg, var(--card-dark-sheen) 0%, var(--card-dark) 35%, var(--card-dark) 100%);
    color: var(--name-white);
    text-align: center;
  }
  .brand {
    color: var(--logo-grey);
    font-weight: 700;
    text-align: center;
    line-height: 1;
  }
  .brand__line { display: block; }
  .brand__main { font-size: 44px; letter-spacing: -0.5px; }
  .brand__sub { font-size: 36px; margin-top: 4px; }
  .brand__tail { font-size: 15px; margin-top: 6px; }
  .card--back .brand__main { font-size: 48px; }
  .card--back .brand__sub { font-size: 40px; }
  .card--back .brand__tail { font-size: 16px; }
  .person { padding-top: 44px; }
  .person__name { font-size: 25px; font-weight: 700; color: var(--name-white); }
  .person__name small { font-size: 18px; }
  .person__role { font-size: 13px; color: var(--meta-grey); margin-top: 4px; }
  .contact {
    list-style: none;
    margin-top: 42px;
    font-size: 17px; line-height: 1.45;
    color: var(--contact-grey);
  }
</style>
</head>
<body>
<main class="sheet">
  <section class="card card--front" aria-label="Business card front">
    <div class="card__light">
      <div class="brand">
        <span class="brand__line brand__main">Brightlane</span>
        <span class="brand__line brand__sub">Financial</span>
        <span class="brand__line brand__tail">CPA's Ltd.</span>
      </div>
    </div>
    <div class="card__rule"></div>
    <div class="card__dark">
      <div class="person">
        <p class="person__name">Megan Tolliver <small>CPA</small></p>
        <p class="person__role">Owner</p>
      </div>
      <ul class="contact">
        <li>5553628405</li>
        <li>www.brightlanefin.com</li>
        <li>megan@brightlanefin.com</li>
        <li>P.O. Box 418, Halden Falls WI 53187</li>
      </ul>
    </div>
  </section>

  <section class="card card--back" aria-label="Business card back">
    <div class="card__light">
      <div class="brand">
        <span class="brand__line brand__main">Brightlane</span>
        <span class="brand__line brand__sub">Financial</span>
        <span class="brand__line brand__tail">CPA's Ltd.</span>
      </div>
    </div>
    <div class="card__rule"></div>
    <div class="card__dark"></div>
  </section>
</main>
</body>
</html>
```